Poly Gel bottle Design that stands out for Nail Company

I need a label design for the poly gel polish bottle. We are looking for a design that fit our brand store color and a clean design similar to our competitor.

We have 3 bottle Title: Gel Top Coat, Gel base Coat, Gel Matte Coat
The bottle will be white.

Also I will need 1 label for the extension gel.

Bottle volume is 15ml/0.5 fl oz

Target Market(s)

beauty acrylic nail and poly gel nail

Industry/Entity Type

Nail

Font styles to use
Serif
Decorative

Colors
6c459b

Requirements
Must have
• store color scheme. www.plumcrestshop.com

```html
<!DOCTYPE html>
<html lang="en">
<head>
<meta charset="utf-8">
<title>Plumcrest Gel Top Coat Labels</title>
<link rel="stylesheet" href="https://fonts.googleapis.com/css2?family=Jost:wght@300;400;500&family=Playfair+Display:wght@700;900&display=swap">
<style>
  :root {
    --plum: #6c459b;
    --violet: #a82dbf;
    --magenta: #f50fe6;
    --white: #ffffff;
    --ink: #0a0a0a;
    --page: #ffffff;
  }
  html, body {
    margin: 0;
    padding: 0;
    width: 1200px;
    height: 682px;
    overflow: hidden;
    background: var(--page);
  }
  .label-sheet {
    display: block;
    width: 1200px;
    height: 682px;
  }
  .stop-plum { stop-color: var(--plum); }
  .stop-violet { stop-color: var(--violet); }
  .stop-magenta { stop-color: var(--magenta); }
  .panel { filter: url(#soft-shadow); }
  .white-band, .pick-face { fill: var(--white); }
  .title-serif {
    font-family: "Playfair Display", "Bodoni Moda", serif;
    font-weight: 900;
    fill: var(--white);
  }
  .brand-name {
    font-family: "Jost", "Futura", sans-serif;
    font-weight: 500;
    fill: var(--ink);
  }
  .type-light {
    font-family: "Jost", sans-serif;
    font-weight: 300;
  }
  .type-medium {
    font-family: "Jost", sans-serif;
    font-weight: 500;
  }
  .on-color { fill: var(--white); }
  .on-white { fill: var(--ink); }
  .divider { stroke: var(--white); stroke-width: 2; }
</style>
</head>
<body>
<svg class="label-sheet" viewBox="0 0 1200 682" xmlns="http://www.w3.org/2000/svg">
  <defs>
    <linearGradient id="grad-diagonal" x1="0" y1="0" x2="1" y2="1">
      <stop offset="0" class="stop-plum"/>
      <stop offset="0.5" class="stop-violet"/>
      <stop offset="1" class="stop-magenta"/>
    </linearGradient>
    <linearGradient id="grad-reverse" x1="0" y1="0" x2="1" y2="0">
      <stop offset="0" class="stop-magenta"/>
      <stop offset="0.6" class="stop-violet"/>
      <stop offset="1" class="stop-plum"/>
    </linearGradient>
    <filter id="soft-shadow" x="-10%" y="-10%" width="120%" height="120%">
      <feDropShadow dx="0" dy="0" stdDeviation="12" flood-color="#000" flood-opacity="0.35"/>
    </filter>
  </defs>

  <!-- Wrap label -->
  <g class="label label-wrap">
    <rect class="panel" x="39" y="56" width="547" height="572" fill="url(#grad-diagonal)"/>
    <text class="title-serif" x="312" y="173" font-size="47" text-anchor="middle" textLength="381" lengthAdjust="spacingAndGlyphs">GEL TOP COAT</text>
    <rect class="accent-band" x="39" y="234" width="547" height="27" fill="url(#grad-reverse)"/>
    <rect class="white-band" x="39" y="261" width="547" height="182"/>
    <rect class="accent-band" x="39" y="443" width="547" height="25" fill="url(#grad-reverse)"/>
    <text class="brand-name" x="313" y="390" font-size="96" text-anchor="middle" textLength="370" lengthAdjust="spacingAndGlyphs">plumcrest</text>
    <text class="type-light on-color" x="107" y="542" font-size="36" textLength="145" lengthAdjust="spacingAndGlyphs">GEL NAIL</text>
    <text class="type-medium on-color" x="107" y="582" font-size="38" textLength="148" lengthAdjust="spacingAndGlyphs">POLISH</text>
    <line class="divider" x1="338" y1="524" x2="338" y2="566"/>
    <text class="type-medium on-color" x="438" y="536" font-size="38" textLength="76" lengthAdjust="spacingAndGlyphs">10ml</text>
    <text class="type-light on-color" x="439" y="582" font-size="28" textLength="81" lengthAdjust="spacingAndGlyphs">0.33oz</text>
  </g>

  <!-- Cap label -->
  <g class="label label-cap">
    <rect class="panel" x="615" y="54" width="548" height="574" fill="url(#grad-diagonal)"/>
    <path class="pick-edge" transform="translate(-21 4)" fill="var(--magenta)"
      d="M901 143 C1010 143 1077 180 1077 235 C1077 330 1010 420 940 475 C915 495 888 498 860 480 C790 430 745 340 730 280 C722 250 725 235 725 230 C728 170 810 143 901 143 Z"/>
    <path class="pick-face"
      d="M901 143 C1010 143 1077 180 1077 235 C1077 330 1010 420 940 475 C915 495 888 498 860 480 C790 430 745 340 730 280 C722 250 725 235 725 230 C728 170 810 143 901 143 Z"/>
    <text class="brand-name" x="902" y="282" font-size="74" text-anchor="middle" textLength="281" lengthAdjust="spacingAndGlyphs">plumcrest</text>
    <text class="type-light on-white" x="826" y="378" font-size="34" textLength="144" lengthAdjust="spacingAndGlyphs">GEL NAIL</text>
    <text class="type-medium on-white" x="826" y="418" font-size="36" textLength="147" lengthAdjust="spacingAndGlyphs">POLISH</text>
    <text class="type-medium on-color" x="1053" y="417" font-size="33" textLength="63" lengthAdjust="spacingAndGlyphs">10ml</text>
    <text class="type-light on-color" x="1053" y="453" font-size="24" textLength="68" lengthAdjust="spacingAndGlyphs">0.33oz</text>
    <text class="type-medium on-color" x="894" y="577" font-size="56" text-anchor="middle" textLength="305" lengthAdjust="spacingAndGlyphs">Gel Top Coat</text>
  </g>
</svg>
</body>
</html>
```